Security Mobile Patrol Vehicle Wrap

We need a car wrap design for a security service company based in Malaysia called Red Cedar Security.

We provide security guards, security solutions and central monitoring services for our clients. Our clients are factories, commercial buildings, residential areas, resorts and etc

The design should communicate masculine, safe, reliable, trustworthy and young.
The design style that we like is minimal.
The design should be able to use on multiple types of vehicles.
The main vehicle will be as below.
1) Kelmaro Tivan – Sedan
2) Kelmaro Luma RTX - Sedan
3) Varenko Trax – Pickup Truck
4) Nemora Quill – Van
All the vehicle colours will be WHITE.
The design needs to incorporate our logo, website address and the word mobile patrol. We need a design for the vehicle's side, front and back.

Project just got started on April 19 but the current deadline shows April 17.

Industry/Entity Type

Security Services

Requirements
Must have
• website address, logo
Should not have
• Avoid going onto the windows.

```html
<!DOCTYPE html>
<html lang="en">
<head>
<meta charset="utf-8">
<title>Red Cedar Security – Mobile Patrol Vehicle Wrap</title>
<link rel="stylesheet" href="https://fonts.googleapis.com/css2?family=Audiowide&family=Montserrat:wght@700&family=Open+Sans:wght@500&family=Orbitron:wght@700&display=swap">
<style>
  :root {
    --wrap-black: #1d1c16;
    --wrap-yellow: #f2bd1d;
    --panel-black: #000000;
    --digit-white: #ffffff;
    --canvas-white: #ffffff;
  }
  html, body {
    margin: 0;
    padding: 0;
    width: 1200px;
    height: 900px;
    overflow: hidden;
    background: var(--canvas-white);
  }
  .wrap-canvas {
    display: block;
    width: 1200px;
    height: 900px;
  }
  .stripe-dark { fill: var(--wrap-black); }
  .stripe-gold { fill: var(--wrap-yellow); }
  .brand-name {
    font-family: "Montserrat", sans-serif;
    font-weight: 700;
    fill: var(--wrap-black);
  }
  .brand-name--main { font-size: 40px; letter-spacing: 1px; }
  .brand-name--sub { font-size: 15px; letter-spacing: 11px; }
  .web-panel {
    fill: var(--panel-black);
    stroke: var(--wrap-yellow);
    stroke-width: 2.5;
  }
  .globe-icon {
    fill: none;
    stroke: var(--wrap-yellow);
    stroke-width: 2;
  }
  .web-address {
    font-family: "Open Sans", sans-serif;
    font-weight: 500;
    font-size: 18px;
    fill: var(--wrap-yellow);
  }
  .phone-panel {
    fill: var(--wrap-black);
    stroke: var(--wrap-yellow);
    stroke-width: 2.5;
  }
  .phone-number {
    font-family: "Orbitron", sans-serif;
    font-weight: 700;
    font-size: 28px;
    fill: var(--digit-white);
  }
  .patrol-ribbon {
    fill: var(--wrap-black);
    stroke: var(--wrap-yellow);
    stroke-width: 2;
    stroke-linejoin: round;
  }
  .patrol-label {
    font-family: "Audiowide", sans-serif;
    font-size: 13.5px;
    fill: var(--wrap-yellow);
    text-anchor: middle;
  }
</style>
</head>
<body>
<svg class="wrap-canvas" viewBox="0 0 1200 900" xmlns="http://www.w3.org/2000/svg" aria-label="Red Cedar Security mobile patrol vehicle side wrap">
  <g class="body-stripes">
    <polygon class="stripe-gold" points="76.4,470.2 196.4,470.2 180,481.1"/>
    <polygon class="stripe-dark" points="177.3,404.7 676.4,385.7 1129.1,485.5 630,504.6"/>
    <polygon class="stripe-gold" points="177.3,404.7 810,417.4 785,477.8 1129.1,485.5 630,504.6"/>
  </g>

  <g class="brand">
    <text class="brand-name brand-name--main" x="486" y="472" textLength="282" lengthAdjust="spacingAndGlyphs">RED CEDAR</text>
    <text class="brand-name brand-name--sub" x="624" y="496">SECURITY</text>
  </g>

  <g class="web-badge">
    <polygon class="web-panel" points="762,332.8 1055.5,402 1043.5,461 751.7,391.7"/>
    <g class="globe-icon">
      <circle cx="786.6" cy="369.3" r="23"/>
      <ellipse cx="786.6" cy="369.3" rx="10" ry="23" transform="rotate(13 786.6 369.3)"/>
      <line x1="786.6" y1="346.3" x2="786.6" y2="392.3" transform="rotate(13 786.6 369.3)"/>
      <line x1="763.6" y1="369.3" x2="809.6" y2="369.3" transform="rotate(13 786.6 369.3)"/>
      <line x1="767" y1="357.5" x2="806" y2="357.5" transform="rotate(13 786.6 369.3)"/>
      <line x1="767" y1="381" x2="806" y2="381" transform="rotate(13 786.6 369.3)"/>
    </g>
    <text class="web-address" x="821" y="378" transform="rotate(13.3 821 378)" textLength="222" lengthAdjust="spacingAndGlyphs">https://redcedarsecurity.my</text>
  </g>

  <g class="phone-badge">
    <polygon class="phone-panel" points="643.6,510 971,499 972,533.5 644.8,548.2"/>
    <text class="phone-number" x="656" y="537" transform="rotate(-2 656 537)" textLength="300" lengthAdjust="spacingAndGlyphs">123456789</text>
  </g>

  <g class="patrol-badge">
    <polygon class="patrol-ribbon" points="441.8,531.8 417.3,539 436.4,551 425.5,571.6 450.5,565.6"/>
    <polygon class="patrol-ribbon" points="559,531.8 583.7,539 564.5,551 576.5,571.6 551,565.6"/>
    <path class="patrol-ribbon" d="M433.6,496.4 Q500,478 567.3,496.4 L551,565.6 Q500,556 450.5,565.6 Z"/>
    <text class="patrol-label" x="500.5" y="522">WORD MOBILE</text>
    <text class="patrol-label" x="504" y="540">PATROL</text>
  </g>
</svg>
</body>
</html>
```